New Business Cards for Organic Meat Farm

We need a business card designed for Thornbury Farm, a meat farm in western MA. Our logo uses a hand-drawn woodcut (attached). Our color palette has been simply black and white (shown in notepad and picture of our food truck). While we are based out of western MA, we have ambitions to grow nationally, so our hope is for a classy and memorable card which will be printed on a premium quality stock from a printer like printkestrel.com.
Target Market(s)
consumers of quality meats, restauranteurs, partnering farms
Industry/Entity Type
Farming and prepared meat products
Contact Information for Business Card
Wendell Pruitt, President/Owner, wendell@thornburyfarm.com, mobile: 413-555-0172, phone: 413-555-0148, thornburyfarm.com, facebook: @thornburyfarm, instagram: @thornburyfarmma
Colors
Designer to choose colors to be used in the design.
Look and feel

```html
<!DOCTYPE html>
<html lang="en">
<head>
<meta charset="utf-8">
<title>Thornbury Farm Business Card</title>
<link rel="stylesheet" href="https://fonts.googleapis.com/css2?family=Montserrat:wght@400;600;800&display=swap">
<style>
  :root {
    --ink: #111111;
    --paper: #ffffff;
    --stage: #2a2a2a;
    --rule: #1a1a1a;
    --soft-ink: #222222;
  }
  * { margin: 0; padding: 0; box-sizing: border-box; }
  html, body { width: 1200px; height: 1186px; overflow: hidden; }
  body {
    background: var(--stage);
    font-family: "Montserrat", sans-serif;
    position: relative;
  }
  .card {
    position: absolute;
    width: 700px;
    height: 400px;
    border-radius: 26px;
    overflow: hidden;
  }
  .card--back { left: 250px; top: 150px; background: var(--ink); color: var(--paper); }
  .card--front { left: 250px; top: 636px; background: var(--paper); color: var(--ink); }

  .brand { position: absolute; left: 0; right: 0; text-align: center; }
  .brand__mark {
    display: inline-block; width: 14px; height: 14px; border-radius: 50%;
    background: currentColor; vertical-align: middle; margin-right: 12px;
  }
  .brand__name {
    font-weight: 600; font-size: 46px; letter-spacing: 1px; vertical-align: middle;
  }
  .card--back .brand { top: 168px; }
  .card--front .brand { top: 96px; width: 460px; }
  .card--front .brand__name { font-size: 38px; }

  .social {
    position: absolute; display: flex; align-items: center; gap: 8px;
    font-size: 15px; font-weight: 400;
  }
  .social__dot { width: 13px; height: 13px; border-radius: 50%; background: var(--ink); }
  .social--instagram { left: 470px; top: 70px; }
  .social--facebook { left: 36px; top: 268px; }

  .holder { position: absolute; left: 150px; top: 296px; width: 260px; text-align: center; }
  .holder__name { font-weight: 800; font-size: 26px; letter-spacing: 0.5px; }
  .holder__role { font-size: 15px; color: var(--soft-ink); }

  .divider {
    position: absolute; left: 425px; top: 212px; width: 2px; height: 82px; background: var(--rule);
  }
  .contacts {
    position: absolute; left: 448px; top: 206px; list-style: none;
    font-size: 16px; line-height: 29px;
  }
  .contacts li { display: flex; align-items: center; gap: 10px; }
  .contacts svg { width: 14px; height: 14px; fill: var(--ink); flex: none; }
</style>
</head>
<body>
  <section class="card card--back">
    <div class="brand">
      <span class="brand__mark"></span><span class="brand__name">Thornbury Farm</span>
    </div>
  </section>

  <section class="card card--front">
    <div class="brand">
      <span class="brand__mark"></span><span class="brand__name">Thornbury Farm</span>
    </div>

    <div class="social social--instagram"><span class="social__dot"></span>@thornburyfarmma</div>
    <div class="social social--facebook"><span class="social__dot"></span>@thornburyfarm</div>

    <div class="holder">
      <div class="holder__name">WENDELL PRUITT</div>
      <div class="holder__role">President/Owner</div>
    </div>

    <div class="divider"></div>

    <ul class="contacts">
      <li>
        <svg viewBox="0 0 14 14"><path d="M4 0h6a1.5 1.5 0 0 1 1.5 1.5v11A1.5 1.5 0 0 1 10 14H4a1.5 1.5 0 0 1-1.5-1.5v-11A1.5 1.5 0 0 1 4 0zm0.3 1.6v9.2h5.4V1.6zM7 11.6a0.9 0.9 0 1 0 0 1.8a0.9 0.9 0 0 0 0-1.8z"/></svg>
        413-555-0172
      </li>
      <li>
        <svg viewBox="0 0 14 14"><path d="M1 4.5C1 3 3 2 7 2s6 1 6 2.5V6h-3V4.6C9 4.3 8 4.2 7 4.2S5 4.3 4 4.6V6H1zM3.5 7h7l1.5 5.5H2z"/></svg>
        413-555-0148
      </li>
      <li>
        <svg viewBox="0 0 14 14"><circle cx="7" cy="7" r="6.5"/><path d="M1 7h12M7 0.8c-2.2 2-2.2 10.4 0 12.4M7 0.8c2.2 2 2.2 10.4 0 12.4" stroke="#fff" stroke-width="0.9" fill="none"/></svg>
        thornburyfarm.com
      </li>
    </ul>
  </section>
</body>
</html>
```